Business Card Design

We need a business card designed which uses our logo and looks really good. The company is called LumaPivot482. We help e-commerce companies reduce cart abandonment by rescuing the sale through our innovative technology.

Our corporate colors are red, black and white.

I have attached our AI file for the logo as well.
Updates

Additional information for the business card:

Name: Derek Malloy
Title: President/CTO
Phone: 1-855-LUMA-482
Website: www.lumapivot482.com
Email: derek@lumapivot482.com

Tag line: Guiding Browsers To Checkout

Industry/Entity Type

E-Commerce

```html
<!DOCTYPE html>
<html lang="en">
<head>
<meta charset="utf-8">
<title>LumaPivot482 Business Card</title>
<link rel="stylesheet" href="https://fonts.googleapis.com/css2?family=Arimo:wght@400;700&display=swap">
<style>
  :root {
    --backdrop: #2f2f2f;
    --card-white: #ffffff;
    --tagline-strip: #ececec;
    --card-grey: #6e6e6e;
    --brand-red: #e3232b;
    --brand-black: #151515;
    --text-light: #ffffff;
  }
  * { box-sizing: border-box; margin: 0; padding: 0; }
  html, body {
    width: 1200px; height: 1000px; overflow: hidden;
    background: var(--backdrop);
    font-family: "Arimo", Arial, sans-serif;
  }
  .canvas {
    width: 1200px; height: 1000px;
    display: flex; align-items: center; justify-content: center;
  }
  .business-card {
    width: 840px; height: 480px;
    border-radius: 44px;
    overflow: hidden;
    background: var(--card-grey);
    display: flex; flex-direction: column;
  }
  .brand-band {
    height: 170px;
    background: var(--card-white);
    display: flex; align-items: center; justify-content: center;
    gap: 22px;
  }
  .brand-mark {
    width: 40px; height: 40px;
    background: var(--brand-red);
  }
  .brand-name {
    font-size: 74px; font-weight: 400;
    color: var(--brand-black);
    letter-spacing: 1px;
  }
  .tagline-strip {
    height: 58px;
    background: var(--tagline-strip);
    display: flex; align-items: center;
    padding-left: 70px;
  }
  .tagline {
    color: var(--brand-red);
    font-size: 24px;
    letter-spacing: 4px;
    word-spacing: 10px;
    text-transform: uppercase;
    white-space: nowrap;
  }
  .details {
    flex: 1;
    display: flex; justify-content: space-between; align-items: center;
    padding: 0 60px;
    color: var(--text-light);
  }
  .person { white-space: nowrap; }
  .person-name {
    font-size: 50px; letter-spacing: 3px; line-height: 1.25;
  }
  .person-title {
    font-size: 44px; letter-spacing: 3px; line-height: 1.25;
  }
  .contact-list { list-style: none; display: flex; flex-direction: column; gap: 22px; }
  .contact-item {
    display: flex; align-items: center; gap: 18px;
    font-size: 20px; letter-spacing: 1.5px;
    white-space: nowrap;
  }
  .contact-icon { width: 26px; height: 26px; flex: none; }
</style>
</head>
<body>
<main class="canvas">
  <article class="business-card">
    <header class="brand-band">
      <span class="brand-mark"></span>
      <span class="brand-name">LumaPivot482</span>
    </header>
    <div class="tagline-strip">
      <p class="tagline">Guiding Browsers To Checkout</p>
    </div>
    <section class="details">
      <div class="person">
        <p class="person-name">Derek Malloy</p>
        <p class="person-title">President/CTO</p>
      </div>
      <ul class="contact-list">
        <li class="contact-item">
          <svg class="contact-icon" viewBox="0 0 24 24" aria-hidden="true"><path fill="#fff" d="M6.6 10.8a15.1 15.1 0 0 0 6.6 6.6l2.2-2.2c.3-.3.7-.4 1-.2 1.1.4 2.3.6 3.6.6.6 0 1 .4 1 1V20c0 .6-.4 1-1 1A17 17 0 0 1 3 4c0-.6.4-1 1-1h3.5c.6 0 1 .4 1 1 0 1.3.2 2.5.6 3.6.1.3 0 .7-.2 1z"/></svg>
          <span>1-855-LUMA-482</span>
        </li>
        <li class="contact-item">
          <svg class="contact-icon" viewBox="0 0 24 24" aria-hidden="true"><circle cx="12" cy="12" r="10" fill="none" stroke="#fff" stroke-width="2"/><path d="M2 12h20M12 2c3 3 3 17 0 20M12 2c-3 3-3 17 0 20" fill="none" stroke="#fff" stroke-width="1.6"/></svg>
          <span>www.lumapivot482.com</span>
        </li>
        <li class="contact-item">
          <svg class="contact-icon" viewBox="0 0 24 24" aria-hidden="true"><rect x="2" y="5" width="20" height="14" fill="#fff"/><path d="M2 5l10 8 10-8" fill="none" stroke="#6e6e6e" stroke-width="1.6"/></svg>
          <span>derek@lumapivot482.com</span>
        </li>
      </ul>
    </section>
  </article>
</main>
</body>
</html>
```